Printing company needs stellar web site!

We need a website for a printing company based in Atlanta, Georgia, USA. Our company is 26 years old and just this year did a logo and branding refresh. Now we need our website to be refreshed as well.

Please see the attached source files for our new logo and stationary design.

Industry/Entity Type

Printing

```html
<!DOCTYPE html>
<html lang="en">
<head>
<meta charset="utf-8">
<title>Inkstone Printing</title>
<link rel="stylesheet" href="https://fonts.googleapis.com/css2?family=Open+Sans:wght@400;600;700&family=Oswald:wght@300;400&family=Lora:ital@1&display=swap">
<style>
  :root {
    --brand-blue: #0b62a8;
    --brand-blue-dark: #0a4f8c;
    --nav-black: #0b0b0b;
    --link-blue: #1d72b8;
    --text-grey: #6b6b6b;
    --muted-grey: #9a9a9a;
    --card-top: #1f8ac8;
    --card-bottom: #0a5b99;
    --orange-top: #ffa11c;
    --orange-bottom: #ff7a00;
    --white: #ffffff;
  }
  * { box-sizing: border-box; margin: 0; padding: 0; }
  html, body { width: 1200px; height: 912px; overflow: hidden; background: var(--white); }
  body { position: relative; font-family: "Open Sans", Arial, sans-serif; color: var(--text-grey); }
  a { color: inherit; text-decoration: none; }

  .site-header { position: absolute; left: 0; top: 0; width: 1200px; height: 79px; background: var(--brand-blue); }
  .rainbow-rule { position: absolute; left: 0; width: 1200px; height: 3px;
    background: linear-gradient(90deg, #2b3a8f, #c2185b 25%, #e53935 45%, #fbc02d 60%, #43a047 78%, #1e88e5); }
  .site-header .rainbow-rule { top: 77px; }

  .brand { position: absolute; left: 198px; top: 14px; }
  .brand-name { font-weight: 700; font-size: 38px; line-height: 38px; color: var(--white); letter-spacing: 1px; }
  .brand-tagline { margin-top: 4px; font-size: 9.5px; font-weight: 600; color: var(--white); letter-spacing: .2px; text-transform: uppercase; }

  .phones { position: absolute; right: 228px; top: 12px; display: flex; gap: 20px; font-size: 17px; color: var(--white); }
  .phones span.sep { font-size: 10px; line-height: 24px; }
  .account-links { position: absolute; right: 228px; top: 49px; display: flex; gap: 12px; font-size: 10px; font-weight: 700; color: var(--white); text-transform: uppercase; }

  .main-nav { position: absolute; left: 0; top: 80px; width: 1200px; height: 21px; background: var(--nav-black); font-size: 10.5px; color: #e6e6e6; }
  .main-nav .primary { position: absolute; left: 200px; top: 3px; display: flex; gap: 18px; }
  .main-nav .secondary { position: absolute; right: 205px; top: 3px; display: flex; gap: 18px; color: #9a9a9a; }

  .menu-group { position: absolute; left: 199px; }
  .menu-group h2 { font-size: 16.5px; line-height: 20px; font-weight: 400; color: var(--link-blue); }
  .menu-group p { font-size: 9px; line-height: 14.6px; color: #7a7a7a; white-space: nowrap; }
  .group-print { top: 120px; }
  .group-signage { top: 325px; }
  .group-design { top: 384px; }
  .group-other { top: 413px; }

  .photo { position: absolute; }
  .hero-photo { left: 407px; top: 124px; width: 386px; height: 258px;
    background: linear-gradient(135deg, #c9c6c0 0%, #8b9097 45%, #2d4a8a 70%, #58606a 100%); }
  .thumb { top: 401px; width: 94px; height: 62px; }
  .thumb-1 { left: 407px; background: linear-gradient(135deg, #d0304a, #f2c84b 50%, #4aa0d8); }
  .thumb-2 { left: 505px; background: linear-gradient(135deg, #3a3a3a, #c9c2b4 55%, #5a8a4a); }
  .thumb-3 { left: 602px; background: linear-gradient(135deg, #2a2a2a, #6a7078 50%, #2d5fa0); }
  .thumb-4 { left: 699px; background: linear-gradient(135deg, #9a5a3a, #e6dcd2 55%, #4a4a4a); }

  .promo-photo { position: absolute; left: 827px; top: 124px; width: 173px; height: 129px; border-radius: 8px; overflow: hidden;
    background: linear-gradient(160deg, #2a2a2a 0%, #7a7f88 40%, #c94d5a 70%, #3d8bd1 100%); }
  .promo-photo p { position: absolute; left: 0; right: 0; top: 4px; text-align: center; white-space: nowrap; font-size: 12px; line-height: 14.5px; font-weight: 600; color: var(--white); }

  .price-box { position: absolute; left: 827px; top: 269px; width: 173px; height: 110px; background: var(--brand-blue-dark); border: 2px solid #0c4070; padding: 7px 8px; }
  .price-box h3 { font-family: "Oswald", "Arial Narrow", sans-serif; font-weight: 400; font-size: 13.5px; color: #ffb347; margin-bottom: 6px; white-space: nowrap; text-align: center; }
  .price-box ul { list-style: none; }
  .price-box li { display: flex; justify-content: space-between; font-size: 9.8px; line-height: 13.2px; color: var(--white); padding: 0 6px; }

  .design-cta { position: absolute; left: 827px; top: 392px; width: 173px; height: 71px; border-radius: 8px;
    background: linear-gradient(var(--orange-top), var(--orange-bottom)); display: flex; align-items: center; justify-content: center;
    font-family: "Oswald", "Arial Narrow", sans-serif; font-weight: 300; font-size: 21px; color: var(--white); }

  .intro { position: absolute; left: 200px; top: 491px; width: 800px; text-align: center; white-space: nowrap; font-family: "Lora", Georgia, serif; font-style: italic; font-size: 16px; line-height: 21.5px; color: var(--muted-grey); }

  .step-card { position: absolute; top: 582px; width: 255px; height: 216px; background: linear-gradient(var(--card-top), var(--card-bottom)); border: 1px solid #0b4f86; }
  .step-card h3 { margin-top: 15px; text-align: center; font-size: 20px; line-height: 24px; font-weight: 600; color: var(--white); letter-spacing: .3px; }
  .step-card .step-photo { position: absolute; left: 21px; top: 48px; width: 211px; height: 116px; border: 1px solid #cfe3f2; }
  .step-card p { position: absolute; left: 0; right: 0; top: 173px; text-align: center; white-space: nowrap; font-size: 9.6px; line-height: 13.5px; color: var(--white); }
  .card-1 { left: 206px; } .card-2 { left: 473px; } .card-3 { left: 739px; }
  .card-1 .step-photo { background: linear-gradient(120deg, #f4e1d2, #e0b89c 45%, #f2f2f2); }
  .card-2 .step-photo { background: radial-gradient(circle at 50% 50%, #d8eefa, #6bb4e0 70%, #3a8cc8); }
  .card-3 .step-photo { background: linear-gradient(135deg, #ffffff, #e2e2e2 55%, #b7b7b7); }

  .site-footer { position: absolute; left: 0; top: 834px; width: 1200px; height: 78px; background: var(--nav-black); text-align: center; font-size: 10.3px; }
  .site-footer .rainbow-rule { top: 0; }
  .site-footer .primary { margin-top: 12px; color: #e6e6e6; }
  .site-footer .secondary { margin-top: 2px; color: #8a8a8a; }
  .site-footer .copyright { margin-top: 4px; color: #e6e6e6; }
  .site-footer .bar { margin: 0 5px; }
</style>
</head>
<body>
  <header class="site-header">
    <div class="brand">
      <div class="brand-name">INKSTONE</div>
      <div class="brand-tagline">Fine printing • Fast turnaround • Fair prices.</div>
    </div>
    <div class="phones">
      <span>404.555.0142</span><span class="sep">•</span><span>404.555.0178</span><span class="sep">•</span><span>404.555.0193</span>
    </div>
    <nav class="account-links">
      <a href="#">Log in / My account</a><span>|</span><a href="#">Sign up</a><span>|</span><a href="#">Contact</a><span>|</span><a href="#">About us</a><span>|</span><a href="#">Cart</a>
    </nav>
    <div class="rainbow-rule"></div>
  </header>

  <nav class="main-nav">
    <div class="primary"><a href="#">Home</a><a href="#">Pricing</a><a href="#">Preparing Files</a><a href="#">Download Templates</a><a href="#">Testimonials</a><a href="#">Turnaround Time</a></div>
    <div class="secondary"><a href="#">Samples</a><a href="#">Brokers Program</a><a href="#">Help</a></div>
  </nav>

  <aside class="product-menu">
    <div class="menu-group group-print">
      <h2>Print Products</h2>
      <p>Business Card &nbsp;|&nbsp; Booklet &nbsp;|&nbsp; Bookmark<br>Brochure &nbsp;|&nbsp; Calendar &nbsp;|&nbsp; Catalog &nbsp;|&nbsp; CD<br>Package &nbsp;|&nbsp; Club Flyer &nbsp;|&nbsp; Collectors<br>Card &nbsp;Door Hanger &nbsp;|&nbsp; DVD Package<br>Envelope &nbsp;|&nbsp; Event Ticket &nbsp;|&nbsp; Flyer<br>Hang Tag &nbsp;|&nbsp; Letterhead &nbsp;|&nbsp; Mini Menu<br>Notepad &nbsp;|&nbsp; Poster &nbsp;|&nbsp; Postcard<br>Presentation Folder &nbsp;|&nbsp; Rackcard<br>Rip Business Card &nbsp;|&nbsp; Rolodex &nbsp;|&nbsp; Roll<br>Label &nbsp;|&nbsp; Special Shapes &nbsp;|&nbsp; Staggered<br>Cut Flyer &nbsp;|&nbsp; Sticker &nbsp;|&nbsp; Table Tent<br>Tent Card</p>
    </div>
    <div class="menu-group group-signage">
      <h2>Signage/Banners</h2>
      <p>Banner &nbsp;|&nbsp; Poster (Wide) &nbsp;|&nbsp; Window<br>Cling &nbsp;|&nbsp; Window Decal &nbsp;|&nbsp; Yard Sign</p>
    </div>
    <div class="menu-group group-design"><h2>Design Services</h2></div>
    <div class="menu-group group-other">
      <h2>Other Services</h2>
      <p>Mailing Services &nbsp;|&nbsp; Marketing Services</p>
    </div>
  </aside>

  <div class="photo hero-photo" role="img" aria-label="Press operator working at an offset printing press"></div>
  <div class="photo thumb thumb-1" role="img" aria-label="Colour proof sheets with a loupe"></div>
  <div class="photo thumb thumb-2" role="img" aria-label="Spiral bound notebooks and swatches"></div>
  <div class="photo thumb thumb-3" role="img" aria-label="Technician servicing a printing machine"></div>
  <div class="photo thumb thumb-4" role="img" aria-label="Stack of printed catalogues"></div>

  <div class="promo-photo" role="img" aria-label="Colour bars on a press sheet under a loupe">
    <p>Lorem ipsum dolor sit amet,<br>consectetur adipiscing elit.</p>
  </div>

  <section class="price-box">
    <h3>DONEC LUCTUS NON ARCU IN</h3>
    <ul>
      <li><span>In sed quam tortor</span><span>$ 123</span></li>
      <li><span>Cras id rhoncus velit</span><span>$ 123</span></li>
      <li><span>Curabitur ultricies nisl</span><span>$ 123</span></li>
      <li><span>Quis tellus sollicitudin</span><span>$ 123</span></li>
      <li><span>In semper erat feugiat.</span><span>$ 123</span></li>
    </ul>
  </section>

  <a class="design-cta" href="#">DESIGN SERVICES</a>

  <p class="intro">Lorem ipsum dolor sit amet, consectetur adipiscing elit. Nulla eu tortor sed arcu cursus<br>lobortis sed eu sapien. Vivamus in ullamcorper leo. Maecenas sodales luctus lorem nec iaculis.<br>Nam vitae ultricies orci. Duis id scelerisque justo.</p>

  <section class="step-card card-1">
    <h3>ENTER YOUR INFO</h3>
    <div class="step-photo" role="img" aria-label="Hands typing on a keyboard"></div>
    <p>Maecenas vel est quis orci dictum ornare id vel elit.<br>Cras rhoncus consectetur felis sed pharetra.</p>
  </section>
  <section class="step-card card-2">
    <h3>CHECK YOUR EMAIL</h3>
    <div class="step-photo" role="img" aria-label="Envelope with an at sign"></div>
    <p>Maecenas vel est quis orci dictum ornare id vel elit.<br>Cras rhoncus consectetur felis sed pharetra.</p>
  </section>
  <section class="step-card card-3">
    <h3>FIND SAMPLES</h3>
    <div class="step-photo" role="img" aria-label="Figure holding a magnifying glass"></div>
    <p>Maecenas vel est quis orci dictum ornare id vel elit.<br>Cras rhoncus consectetur felis sed pharetra.</p>
  </section>

  <footer class="site-footer">
    <div class="rainbow-rule"></div>
    <div class="primary">Home<span class="bar">|</span>Pricing<span class="bar">|</span>Preparing Files<span class="bar">|</span>Download Templates<span class="bar">|</span>Testimonials<span class="bar">|</span>Turnaround Time</div>
    <div class="secondary">Samples<span class="bar">|</span>Brokers Program<span class="bar">|</span>Help</div>
    <div class="copyright">© Copyright 2014</div>
  </footer>
</body>
</html>
```